Wellness/ Medical Fitness Company Seeks Promotional Brochure

We need a 4 page brochure for the launch of our new business next month. We are combining science and medicine with the fitness and wellness industry. We are unique in that we are using cutting edge technology and monitoring devices to create customized workouts and training. We offer group classes and individual training.We are looking for a professional promotion brochure that has sleek and modern look and feel to it. We would like to use the colors of our logo in the design. We are a company made up of young people so we would like to have a future and modern vibe to the design.

Target Market(s)

18-65 male and female

Industry/Entity Type

Medical

Colors

Designer to choose colors to be used in the design.

Requirements
Must have
• Modern, sleek look
• Marketing to a professional demographic
Should not have
• No gaudy or tacky colors

```html
<!DOCTYPE html>
<html lang="en">
<head>
<meta charset="utf-8">
<title>Novara Wellness Brochure</title>
<link href="https://fonts.googleapis.com/css2?family=Lato:wght@300;400;700&display=swap" rel="stylesheet">
<style>
  :root{
    --canvas:#ffffff;
    --night:#14171d;
    --night-mid:#262b33;
    --slate:#3a4048;
    --taupe:#8a847d;
    --taupe-light:#bdb6ae;
    --heading:#6f6a65;
    --ink:#1c1c1c;
    --icon:#6f6a65;
    --icon-ring:#9a948d;
    --white:#ffffff;
    --sun:#f7dcb8;
  }
  *{margin:0;padding:0;box-sizing:border-box}
  html,body{width:1200px;height:600px;overflow:hidden;background:var(--canvas)}
  body{position:relative;font-family:"Lato",Arial,sans-serif;color:var(--ink)}
  .panel{position:absolute;top:20px;width:384px;height:497px;overflow:hidden;box-shadow:0 2px 5px rgba(0,0,0,.35)}
  .panel--cover{left:16px}
  .panel--back{left:412px}
  .panel--inside{left:807px;background:var(--white)}

  .photo{position:absolute;inset:0}
  .photo--training{background:radial-gradient(ellipse at 65% 35%,#4a4f57 0%,var(--night-mid) 45%,var(--night) 100%)}
  .photo--wallball{background:linear-gradient(90deg,#1b2029 0%,#2a3038 55%,#59626a 72%,#39414a 100%)}
  .photo--runner{left:auto;right:0;top:0;width:260px;height:210px;bottom:auto;
    background:linear-gradient(90deg,rgba(255,255,255,1) 0%,rgba(251,238,222,.9) 30%,var(--sun) 60%,#e8c39a 100%)}

  .brand{position:absolute;left:0;right:0;text-align:center;color:var(--taupe-light)}
  .brand__mark{display:inline-block;width:40px;height:40px;border-radius:50%;background:var(--taupe);vertical-align:middle;margin-right:10px}
  .brand__name{display:inline-block;vertical-align:middle;font-weight:300;font-size:34px;letter-spacing:3px;color:var(--taupe-light)}
  .panel--cover .brand{top:224px}
  .panel--back .brand{top:228px}

  .contact{position:absolute;left:0;right:0;top:401px;text-align:center;color:var(--white)}
  .contact__title{font-weight:700;font-size:15.5px;letter-spacing:.3px}
  .contact__rule{width:7px;height:1px;background:var(--white);margin:14px auto 13px}
  .contact__line{font-size:6px;line-height:7.6px}

  .intro{position:absolute;left:25px;top:67px;width:135px}
  .section-title{font-weight:400;color:var(--heading);font-size:11.5px;line-height:13.6px;text-transform:uppercase}
  .intro p{margin-top:8px;font-size:6.5px;line-height:8.3px;text-align:justify}
  .about{position:absolute;left:25px;top:244px;width:345px}
  .about p{font-size:6px;line-height:7.6px;margin-top:5px}
  .about .section-title{font-size:11.5px}

  .programs-title{position:absolute;left:0;width:384px;top:318px;text-align:center;font-weight:700;color:var(--heading);font-size:11px;text-transform:uppercase}
  .program{position:absolute;width:80px;margin-left:-40px;text-align:center;font-size:6.4px;line-height:7.6px;color:#444}
  .program svg{display:block;margin:0 auto 4px}
  .band{position:absolute;left:0;right:0;bottom:0;height:16px;background:var(--taupe)}
</style>
</head>
<body>

<section class="panel panel--cover">
  <div class="photo photo--training" role="img" aria-label="Man training with battle ropes in a dark gym"></div>
  <div class="brand"><span class="brand__mark"></span><span class="brand__name">novara wellness</span></div>
</section>

<section class="panel panel--back">
  <div class="photo photo--wallball" role="img" aria-label="Woman throwing a medicine ball beside a concrete pillar with suspension straps"></div>
  <div class="brand"><span class="brand__mark"></span><span class="brand__name">novara wellness</span></div>
  <div class="contact">
    <h2 class="contact__title">FOR MORE INFORMATION</h2>
    <div class="contact__rule"></div>
    <p class="contact__line">Website:&nbsp; www.novarawellness.com</p>
    <p class="contact__line">Photos:&nbsp; photos.novarawellness.com</p>
    <p class="contact__line">Community:&nbsp; community.novarawellness.com</p>
  </div>
</section>

<section class="panel panel--inside">
  <div class="photo photo--runner" role="img" aria-label="Runner in a sleeveless hoodie jogging in warm morning light"></div>

  <div class="intro">
    <h2 class="section-title">Created by doctors.<br>Supported by science</h2>
    <p>Novara Wellness creates personalized data-driven solutions for your wellness goals. We believe in using customized assessments to create wellness ecosystems that fit your daily life.</p>
  </div>

  <div class="about">
    <h2 class="section-title">We are not just any gym or wellness center.</h2>
    <p>We are a science lab that is focused on using your biometric outputs to help you train, rest and recover better.</p>
    <p>Whether you want to hit the ball harder or you want to run faster or you just want to join our group classes to live healthier, we will help you achieve those goals.</p>
    <p>Everything we offer is backed by science and medicine.</p>
  </div>

  <h2 class="programs-title">Programs</h2>

  <div class="program" style="left:84px;top:325px">
    <svg width="44" height="44" viewBox="0 0 44 44"><circle cx="22" cy="22" r="21" fill="none" stroke="var(--icon-ring)" stroke-width="1"/><g fill="var(--icon)"><circle cx="16" cy="18" r="3"/><circle cx="28" cy="18" r="3"/><circle cx="22" cy="16" r="3.4"/><path d="M11 29a5 5 0 0 1 10 0zM23 29a5 5 0 0 1 10 0zM16 28a6 6 0 0 1 12 0z"/></g></svg>
    Group Fitness and<br>Bootcamp Classes
  </div>
  <div class="program" style="left:158px;top:325px">
    <svg width="44" height="44" viewBox="0 0 44 44"><circle cx="22" cy="22" r="21" fill="none" stroke="var(--icon-ring)" stroke-width="1"/><g fill="none" stroke="var(--icon)" stroke-width="1.6" stroke-linecap="round"><circle cx="25" cy="12" r="2.2" fill="var(--icon)" stroke="none"/><path d="M23 16l-3 8 5 3-2 6M20 24l-5 6M18 18l5-2 4 4 3-1"/><path d="M12 33h20"/></g></svg>
    Individualized<br>Training Classes
  </div>
  <div class="program" style="left:234px;top:325px">
    <svg width="44" height="44" viewBox="0 0 44 44"><circle cx="22" cy="22" r="21" fill="none" stroke="var(--icon-ring)" stroke-width="1"/><g fill="none" stroke="var(--icon)" stroke-width="1.5"><circle cx="22" cy="22" r="12"/><circle cx="22" cy="22" r="8.5"/><path d="M22 22l4-5" stroke-linecap="round"/></g></svg>
    Sports Performance<br>Assessment
  </div>
  <div class="program" style="left:307px;top:325px">
    <svg width="44" height="44" viewBox="0 0 44 44"><circle cx="22" cy="22" r="21" fill="none" stroke="var(--icon-ring)" stroke-width="1"/><g fill="none" stroke="var(--icon)" stroke-width="1.6"><path d="M12 20a10 10 0 0 1 17-6M32 24a10 10 0 0 1-17 6"/><path d="M29 10v4h-4M15 34v-4h4"/></g><circle cx="22" cy="22" r="4" fill="var(--icon)"/></svg>
    Metabolic<br>Assessment
  </div>
  <div class="program" style="left:109px;top:401px">
    <svg width="44" height="44" viewBox="0 0 44 44"><circle cx="22" cy="22" r="21" fill="none" stroke="var(--icon-ring)" stroke-width="1"/><g fill="none" stroke="var(--icon)" stroke-width="1.4"><rect x="16" y="10" width="12" height="4"/><rect x="15" y="14" width="14" height="20" rx="2"/><path d="M15 21h14M15 28h14"/></g></svg>
    Dietary Medicine
  </div>
  <div class="program" style="left:190px;top:401px">
    <svg width="44" height="44" viewBox="0 0 44 44"><circle cx="22" cy="22" r="21" fill="none" stroke="var(--icon-ring)" stroke-width="1"/><g fill="var(--icon)"><circle cx="29" cy="17" r="3"/><path d="M11 28l9-6 6 2 4 3-1 2-5-2-5 1-7 2z"/></g></svg>
    Rest and Recovery
  </div>
  <div class="program" style="left:272px;top:401px">
    <svg width="44" height="44" viewBox="0 0 44 44"><circle cx="22" cy="22" r="21" fill="none" stroke="var(--icon-ring)" stroke-width="1"/><g fill="none" stroke="var(--icon)" stroke-width="1.4"><rect x="11" y="13" width="18" height="14" rx="1"/><rect x="27" y="18" width="7" height="13" rx="1"/><path d="M18 17v6l5-3z"/></g></svg>
    Remote Monitoring<br>and Training
  </div>

  <div class="band"></div>
</section>

</body>
</html>
```